We are energy brokers. www.brightvalecurrent.com
We are inviting auto dealers to participate in an energy buyers group that will help them reduce their cost of electricity.
I would like something that can be easily traded out for other industries. ie Gym Owners buyers group, New Business buyers group, etc.
tom@brightvalecurrent.com
877.431.9067 phone

I need this to specifically target "Auto Dealers Energy Buying Group"  
We are targeting only Automobile dealers with this campaign.  Perhaps use a graphic that depicts an auto dealership at night.  Similar to this one.
http://lumenfixturedepot.com/wp-content/uploads/2012/04/auto-dealer-lighting-banner7.jpg

Please use these bullet points:

-Be part of the areas largest Auto Dealers Energy Buying Group
-Reduce energy costs significantly
-Local and professional energy brokers who you can trust
-Free LED lighting analysis available
-Send your latest bill to tom@brightvalecurrent.com to get started

Target Market(s)

Auto Dealers.

Industry/Entity Type

Business

Requirements
Must have
• Brightvale Current logo.
Reduced energy costs equals greater profits.
Free Lighting Analysis.
Energy Costs are at 12 year lows. Great rates available.
Free phone consultation.
http://s21.beta.snapvaultpics.com/user/tomkerrig/media/HHUb.png.html This chart depicts natural gas. Gas determines where energy prices are going. This shows natural gas is cheap right now.

```html
<!DOCTYPE html>
<html lang="en">
<head>
<meta charset="utf-8">
<title>Brightvale Current – Auto Dealers Energy Buying Group</title>
<link href="https://fonts.googleapis.com/css2?family=EB+Garamond:wght@400;600;700;800&display=swap" rel="stylesheet">
<style>
  :root {
    --ink: #111111;
    --ink-soft: #2b2b2b;
    --brand-green: #2f9e3e;
    --brand-mark: #2d4f8a;
    --bullet-yellow: #f2ee1c;
    --play-green: #1fa33a;
    --white: #ffffff;
  }
  html, body {
    margin: 0;
    padding: 0;
    overflow: hidden;
    background: var(--white);
  }
  .flyer {
    position: relative;
    width: 872px;
    height: 1200px;
    overflow: hidden;
    background: var(--white);
    font-family: "EB Garamond", Garamond, Georgia, serif;
    color: var(--ink);
  }
  .backdrop {
    position: absolute;
    inset: 0;
  }
  .brand {
    position: absolute;
    left: 78px;
    top: 38px;
    display: flex;
    align-items: center;
    gap: 16px;
  }
  .brand-dot {
    width: 52px;
    height: 52px;
    border-radius: 50%;
    background: var(--brand-mark);
  }
  .brand-name {
    font-size: 44px;
    font-weight: 600;
    color: var(--brand-green);
    letter-spacing: 0.2px;
  }
  .invite {
    position: absolute;
    left: 0;
    top: 146px;
    width: 872px;
    text-align: center;
    font-weight: 700;
  }
  .invite-lead {
    font-size: 36px;
    line-height: 35px;
  }
  .invite-title {
    font-size: 46px;
    line-height: 62px;
    font-weight: 800;
  }
  .play-icon {
    position: absolute;
    left: 210px;
    top: 452px;
  }
  .benefits {
    position: absolute;
    left: 346px;
    top: 456px;
    width: 490px;
    margin: 0;
    padding: 0;
    list-style: none;
    color: var(--white);
    font-weight: 700;
    font-size: 29px;
    line-height: 32px;
    text-shadow: 0 1px 3px rgba(0,0,0,.6);
  }
  .benefits li {
    position: relative;
    padding-left: 18px;
    margin-bottom: 16px;
  }
  .benefits li::before {
    content: "";
    position: absolute;
    left: 0;
    top: 9px;
    width: 11px;
    height: 11px;
    background: var(--bullet-yellow);
  }
  .contact {
    position: absolute;
    left: 0;
    top: 1046px;
    width: 872px;
    text-align: center;
    color: var(--ink-soft);
  }
  .contact-lead {
    font-size: 30px;
    line-height: 36px;
  }
  .contact-email {
    font-size: 29px;
    font-weight: 700;
    line-height: 36px;
    color: var(--ink);
  }
  .contact-phone {
    font-size: 47px;
    font-weight: 600;
    line-height: 60px;
    color: var(--ink);
  }
</style>
</head>
<body>
<div class="flyer">
  <svg class="backdrop" width="872" height="1200" viewBox="0 0 872 1200">
    <defs>
      <linearGradient id="headerWash" x1="0" y1="0" x2="0" y2="1">
        <stop offset="0" stop-color="#e6f6fa"/>
        <stop offset="1" stop-color="#ffffff"/>
      </linearGradient>
      <linearGradient id="skyTone" x1="0" y1="0" x2="1" y2="0">
        <stop offset="0" stop-color="#f7c77c"/>
        <stop offset="0.5" stop-color="#fbd79a"/>
        <stop offset="1" stop-color="#f39a22"/>
      </linearGradient>
      <radialGradient id="sunGlow" cx="700" cy="220" r="170" gradientUnits="userSpaceOnUse">
        <stop offset="0" stop-color="#ffffff"/>
        <stop offset="0.25" stop-color="#fff2cf" stop-opacity="0.9"/>
        <stop offset="1" stop-color="#fbd79a" stop-opacity="0"/>
      </radialGradient>
      <linearGradient id="waterBand" x1="0" y1="0" x2="0" y2="1">
        <stop offset="0" stop-color="#4fb0ec"/>
        <stop offset="1" stop-color="#1b6fc8"/>
      </linearGradient>
      <linearGradient id="rooftopTone" x1="0" y1="0" x2="0" y2="1">
        <stop offset="0" stop-color="#8a8478"/>
        <stop offset="0.18" stop-color="#4a4e5c"/>
        <stop offset="0.45" stop-color="#243a80"/>
        <stop offset="0.8" stop-color="#2b3f86"/>
        <stop offset="1" stop-color="#5a5a5e"/>
      </linearGradient>
      <linearGradient id="footerGreen" x1="0" y1="0" x2="0" y2="1">
        <stop offset="0" stop-color="#6cc531"/>
        <stop offset="1" stop-color="#a6e04c"/>
      </linearGradient>
    </defs>

    <rect x="16" y="0" width="842" height="320" fill="url(#headerWash)"/>

    <g role="img" aria-label="Warm sunset sky with a bright sun on the right">
      <path d="M16 138 C 220 96, 470 150, 660 118 C 760 102, 820 96, 858 92 L858 320 L16 320 Z" fill="url(#skyTone)"/>
      <path d="M16 138 C 220 96, 470 150, 660 118 C 760 102, 820 96, 858 92 L858 320 L16 320 Z" fill="url(#sunGlow)"/>
    </g>

    <path d="M16 306 C 200 282, 420 270, 600 300 C 720 318, 800 300, 858 286 L858 400 L16 400 Z" fill="url(#waterBand)"/>

    <path d="M16 402 C 260 372, 520 380, 700 396 C 780 402, 830 392, 858 384 L858 1040 L16 1040 Z"
          fill="url(#rooftopTone)" stroke="#ffffff" stroke-width="4"
          role="img" aria-label="Rows of solar panels on a flat commercial rooftop under a clear sky"/>

    <path d="M16 1028 C 220 1010, 520 1040, 700 1018 C 780 1008, 830 1006, 858 1008 L858 1194 L16 1194 Z"
          fill="url(#footerGreen)" stroke="#ffffff" stroke-width="4"/>
  </svg>

  <div class="brand">
    <div class="brand-dot"></div>
    <div class="brand-name">brightvalecurrent</div>
  </div>

  <div class="invite">
    <div class="invite-lead">You are invited</div>
    <div class="invite-lead">to participate in an</div>
    <div class="invite-title">Auto Dealers Energy Buying Group</div>
  </div>

  <svg class="play-icon" width="66" height="66" viewBox="0 0 66 66" aria-hidden="true">
    <circle cx="33" cy="33" r="31" fill="var(--play-green)" stroke="#ffffff" stroke-width="2"/>
    <path d="M25 18 L49 33 L25 48 Z" fill="#ffffff"/>
  </svg>

  <ul class="benefits">
    <li>Be part of the area's largest Auto Dealers Energy Buying Group.</li>
    <li>Reduce energy costs significantly. Reduced energy costs equals greater profits.</li>
    <li>Local and professional energy brokers who you can trust.</li>
    <li>Free LED Lighting Analysis.</li>
    <li>Energy Costs are at 12 year lows. Great rates available.</li>
    <li>Free phone consultation.</li>
    <li>Send your latest bill to tom@brightvalecurrent.com to get started.</li>
  </ul>

  <div class="contact">
    <div class="contact-lead">For more information contact</div>
    <div class="contact-email">tom@brightvalecurrent.com</div>
    <div class="contact-phone">877.431.9067</div>
  </div>
</div>
</body>
</html>
```